Label/sheets for packaging/boxing

We need a label to go on our shipping boxes. Also a time to reorder label or card to put into boxes. We want to use this in different sizes. I want our logo, which we will provide to be used on all items.I would like a flag and eagle ( I will provide file) to be graduated screen tint in upper left or the left side and my company logo and information to be on top solid.....or any design that is better than this idea...I would like the label 4x2.5 inched landscape......I would like to use the file to print different size labels.
Really, the design can be anything using my logo........I'm open for design.
Also, a time to re-order card or label with logo and info, it can include a thank you for ordering from us................confidence, etc. I really want this to stand out and look great.
Updates

Project Deadline Extended
Reason: We are able to add more time to project. Thanks.

Target Market(s)

Business, City accounts.

Industry/Entity Type

Shipping

Requirements
Must have
• Name address contact information, web address....ect.

Eco friendly....
Professional

```html
<!DOCTYPE html>
<html lang="en">
<head>
<meta charset="utf-8">
<title>Shipping Label Sizes</title>
<link rel="stylesheet" href="https://fonts.googleapis.com/css2?family=Special+Elite&family=Archivo+Narrow:wght@400;700&display=swap">
<style>
  :root{
    --kraft:#d3a57a;
    --card:#ffffff;
    --paper:#f4f3f1;
    --navy:#1b3766;
    --maroon:#8c1446;
    --flag-red:#b51d2c;
    --rule:#3a4f7a;
    --ink:#1d1d1d;
  }
  *{margin:0;padding:0;box-sizing:border-box}
  html,body{width:849px;height:1200px;overflow:hidden}
  body{background:var(--kraft);position:relative;font-family:"Archivo Narrow",Arial,sans-serif}

  .label{
    position:absolute;width:712px;height:500px;
    background:var(--card);border-radius:42px;
    transform-origin:top left;
    box-shadow:0 2px 6px rgba(60,35,10,.25);
  }
  .label--small{left:263px;top:40px;transform:scale(.421)}
  .label--medium{left:163px;top:281px;transform:scale(.702)}
  .label--large{left:65px;top:627px}

  .label__face{
    position:absolute;inset:13px;border-radius:32px;overflow:hidden;
    background:linear-gradient(160deg,#fbfbfa,var(--paper) 60%,#ecebe8);
  }
  .label__photo{
    position:absolute;left:0;top:0;width:410px;height:100%;
    background:
      linear-gradient(90deg,rgba(244,243,241,0) 62%,var(--paper) 100%),
      linear-gradient(180deg,rgba(40,35,32,0) 70%,rgba(40,35,32,.55) 100%),
      linear-gradient(135deg,#3a4d80 0%,#8a5a78 28%,#c9424f 48%,#e3d6d4 72%,#eeeae7 100%);
  }
  .label__eco-band{
    position:absolute;left:0;bottom:0;width:76px;height:118px;
    background:var(--flag-red);
    display:flex;align-items:center;justify-content:center;
  }
  .label__scribbles{
    position:absolute;left:622px;top:25px;width:64px;height:425px;
    background:linear-gradient(180deg,#f5d33a 0%,#f08a2a 18%,#e9407a 36%,#c16bc2 56%,#7d6fc6 72%,#2aa7d5 100%);
    -webkit-mask:linear-gradient(90deg,transparent 0%,#000 55%);
            mask:linear-gradient(90deg,transparent 0%,#000 55%);
    opacity:.8;
  }

  .brand{
    position:absolute;left:402px;top:50px;width:200px;
    display:flex;align-items:center;gap:10px;
  }
  .brand__mark{width:30px;height:30px;background:var(--maroon);flex:none}
  .brand__name{
    font-weight:700;font-size:32px;line-height:1.05;color:var(--navy);
  }

  .contact{position:absolute;left:360px;top:240px;width:276px}
  .contact__row{display:flex;align-items:baseline;height:29.5px}
  .contact__key{
    font-family:"Special Elite",Courier,monospace;font-size:15px;
    width:66px;flex:none;color:var(--navy);
  }
  .contact__key--accent{color:var(--maroon)}
  .contact__value{
    flex:1;font-size:17px;color:var(--ink);white-space:nowrap;
    border-bottom:1px solid var(--rule);padding-left:2px;line-height:21px;
  }
  .contact__value--web{border-bottom-color:var(--maroon)}
  .contact__value--cont{padding-left:34px}
  .contact__value--fax{padding-left:24px}
</style>
</head>
<body>

<div class="label label--small">
  <div class="label__face">
    <div class="label__photo" role="img" aria-label="Flag and eagle photograph, fading to white on the right"></div>
    <div class="label__eco-band">
      <svg width="44" height="44" viewBox="0 0 44 44" role="img" aria-label="Recycling symbol">
        <g fill="none" stroke="#fff" stroke-width="4.5" stroke-linejoin="round">
          <path d="M15 17 L22 6 L29 17"/><path d="M33 24 L38 34 L25 34"/><path d="M19 34 L6 34 L11 24"/>
        </g>
      </svg>
    </div>
    <div class="label__scribbles" role="img" aria-label="Colourful crayon scribbles"></div>
    <div class="brand"><span class="brand__mark"></span><span class="brand__name">Harbor Quick Print</span></div>
    <div class="contact">
      <div class="contact__row"><span class="contact__key">Name</span><span class="contact__value">Harbor Quick Print</span></div>
      <div class="contact__row"><span class="contact__key">Address</span><span class="contact__value">482 Maple Avenue</span></div>
      <div class="contact__row"><span class="contact__key"></span><span class="contact__value contact__value--cont">Linden, CA. 95236</span></div>
      <div class="contact__row"><span class="contact__key">Phone</span><span class="contact__value">(209) 555-01482</span></div>
      <div class="contact__row"><span class="contact__key">Fax</span><span class="contact__value contact__value--fax">(209) 555-0193</span></div>
      <div class="contact__row"><span class="contact__key contact__key--accent">Email</span><span class="contact__value">Email: hqprint@mailbox.com</span></div>
      <div class="contact__row"><span class="contact__key contact__key--accent">Web</span><span class="contact__value contact__value--web">www.harborquickprint.com</span></div>
    </div>
  </div>
</div>

<div class="label label--medium">
  <div class="label__face">
    <div class="label__photo" role="img" aria-label="Flag and eagle photograph, fading to white on the right"></div>
    <div class="label__eco-band">
      <svg width="44" height="44" viewBox="0 0 44 44" role="img" aria-label="Recycling symbol">
        <g fill="none" stroke="#fff" stroke-width="4.5" stroke-linejoin="round">
          <path d="M15 17 L22 6 L29 17"/><path d="M33 24 L38 34 L25 34"/><path d="M19 34 L6 34 L11 24"/>
        </g>
      </svg>
    </div>
    <div class="label__scribbles" role="img" aria-label="Colourful crayon scribbles"></div>
    <div class="brand"><span class="brand__mark"></span><span class="brand__name">Harbor Quick Print</span></div>
    <div class="contact">
      <div class="contact__row"><span class="contact__key">Name</span><span class="contact__value">Harbor Quick Print</span></div>
      <div class="contact__row"><span class="contact__key">Address</span><span class="contact__value">482 Maple Avenue</span></div>
      <div class="contact__row"><span class="contact__key"></span><span class="contact__value contact__value--cont">Linden, CA. 95236</span></div>
      <div class="contact__row"><span class="contact__key">Phone</span><span class="contact__value">(209) 555-01482</span></div>
      <div class="contact__row"><span class="contact__key">Fax</span><span class="contact__value contact__value--fax">(209) 555-0193</span></div>
      <div class="contact__row"><span class="contact__key contact__key--accent">Email</span><span class="contact__value">Email: hqprint@mailbox.com</span></div>
      <div class="contact__row"><span class="contact__key contact__key--accent">Web</span><span class="contact__value contact__value--web">www.harborquickprint.com</span></div>
    </div>
  </div>
</div>

<div class="label label--large">
  <div class="label__face">
    <div class="label__photo" role="img" aria-label="Flag and eagle photograph, fading to white on the right"></div>
    <div class="label__eco-band">
      <svg width="44" height="44" viewBox="0 0 44 44" role="img" aria-label="Recycling symbol">
        <g fill="none" stroke="#fff" stroke-width="4.5" stroke-linejoin="round">
          <path d="M15 17 L22 6 L29 17"/><path d="M33 24 L38 34 L25 34"/><path d="M19 34 L6 34 L11 24"/>
        </g>
      </svg>
    </div>
    <div class="label__scribbles" role="img" aria-label="Colourful crayon scribbles"></div>
    <div class="brand"><span class="brand__mark"></span><span class="brand__name">Harbor Quick Print</span></div>
    <div class="contact">
      <div class="contact__row"><span class="contact__key">Name</span><span class="contact__value">Harbor Quick Print</span></div>
      <div class="contact__row"><span class="contact__key">Address</span><span class="contact__value">482 Maple Avenue</span></div>
      <div class="contact__row"><span class="contact__key"></span><span class="contact__value contact__value--cont">Linden, CA. 95236</span></div>
      <div class="contact__row"><span class="contact__key">Phone</span><span class="contact__value">(209) 555-01482</span></div>
      <div class="contact__row"><span class="contact__key">Fax</span><span class="contact__value contact__value--fax">(209) 555-0193</span></div>
      <div class="contact__row"><span class="contact__key contact__key--accent">Email</span><span class="contact__value">Email: hqprint@mailbox.com</span></div>
      <div class="contact__row"><span class="contact__key contact__key--accent">Web</span><span class="contact__value contact__value--web">www.harborquickprint.com</span></div>
    </div>
  </div>
</div>

</body>
</html>
```